Business Card Design for Marketing Firm

Looking for business card design for higher end marketing firm. Clean but impressionable/trendy. We are a marketing firm that represents manufacturers in the foodservice equipment and supply industry. Our customers are end users such has hotels, restaurants, country clubs, convention centers and casinos as well as distributors of restaurants supplies and equipment, and manufacturers of foodservice equipment and supplies.
Target Market(s)
Hotels, Restaurants, Supply & Equipment Distributors, Foodservice Manufacturers
Industry/Entity Type
Foodservice/Hospitality
Contact Information for Business Card
Name, Title, Contact Number, Email, Website, Social Media, Address
Requirements
Must have
- Clean & Simple but Serious and Impressionable

```html
<!DOCTYPE html>
<html lang="en">
<head>
<meta charset="utf-8">
<title>Kestrel Trade Group — Business Card</title>
<link rel="stylesheet" href="https://fonts.googleapis.com/css2?family=Oswald:wght@600&family=Poppins:wght@400;500&display=swap">
<style>
  :root {
    --brand-blue: #050a82;
    --card-white: #ffffff;
    --stage: #1c1c1e;
    --ink-light: #ffffff;
  }
  * { box-sizing: border-box; margin: 0; padding: 0; }
  html, body {
    width: 1200px; height: 900px; overflow: hidden;
    background: var(--stage);
  }
  .canvas {
    width: 1200px; height: 900px;
    display: flex; flex-direction: column; align-items: center; justify-content: center;
    gap: 36px;
  }
  .card {
    position: relative;
    width: 700px; height: 400px;
    overflow: hidden;
    box-shadow: 0 10px 30px rgba(0,0,0,.5);
  }

  /* Front */
  .card-front { background: var(--card-white); }
  .card-front .edge-band {
    position: absolute; left: 0; right: 0; bottom: 0; height: 12px;
    background: var(--brand-blue);
  }
  .brand-lockup {
    position: absolute; left: 0; right: 0; top: 160px;
    display: flex; justify-content: center; align-items: center; gap: 14px;
    color: var(--brand-blue);
  }
  .brand-dot {
    width: 22px; height: 22px; border-radius: 50%;
    background: var(--brand-blue);
  }
  .brand-name {
    font-family: "Poppins", sans-serif; font-weight: 500;
    font-size: 38px; line-height: 1; white-space: nowrap;
  }
  .social-row {
    position: absolute; left: 0; right: 0; bottom: 60px;
    display: flex; justify-content: center; gap: 10px;
  }
  .social-row span {
    width: 22px; height: 22px; border-radius: 50%;
    border: 1.5px solid var(--brand-blue);
  }

  /* Back */
  .card-back { background: var(--brand-blue); color: var(--ink-light); }
  .card-back .edge-band {
    position: absolute; left: 0; right: 0; bottom: 0; height: 16px;
    background: var(--card-white);
  }
  .person {
    position: absolute; left: 40px; top: 150px; width: 300px;
    text-align: right;
  }
  .person-name {
    font-family: "Oswald", sans-serif; font-weight: 600;
    font-size: 34px; text-transform: uppercase; line-height: 1.1;
    white-space: nowrap;
  }
  .person-title {
    font-family: "Poppins", sans-serif; font-weight: 400;
    font-size: 17px; letter-spacing: .5px; white-space: nowrap;
  }
  .divider {
    position: absolute; left: 368px; top: 140px;
    width: 1px; height: 100px; background: rgba(255,255,255,.7);
  }
  .contact-list {
    position: absolute; left: 396px; top: 150px;
    list-style: none;
    font-family: "Poppins", sans-serif; font-size: 16px; letter-spacing: .4px;
  }
  .contact-list li { display: flex; align-items: center; gap: 10px; height: 28px; white-space: nowrap; }
  .contact-list svg { width: 16px; height: 16px; flex: none; }
  .address {
    position: absolute; left: 0; right: 0; bottom: 50px;
    text-align: center;
    font-family: "Poppins", sans-serif; font-size: 16px; letter-spacing: .4px;
  }
</style>
</head>
<body>
<main class="canvas">

  <section class="card card-front" aria-label="Card front">
    <div class="brand-lockup">
      <span class="brand-dot"></span>
      <span class="brand-name">Kestrel Trade Group</span>
    </div>
    <div class="social-row" aria-label="Social media profiles">
      <span></span><span></span><span></span><span></span>
    </div>
    <div class="edge-band"></div>
  </section>

  <section class="card card-back" aria-label="Card back">
    <div class="person">
      <p class="person-name">Daniel Whitmore</p>
      <p class="person-title">Managing Director</p>
    </div>
    <div class="divider"></div>
    <ul class="contact-list">
      <li>
        <svg viewBox="0 0 24 24" fill="none" stroke="currentColor" stroke-width="2" stroke-linecap="round" stroke-linejoin="round"><path d="M22 16.9v3a2 2 0 0 1-2.2 2 19.8 19.8 0 0 1-8.6-3.1 19.5 19.5 0 0 1-6-6A19.8 19.8 0 0 1 2.1 4.2 2 2 0 0 1 4.1 2h3a2 2 0 0 1 2 1.7c.1 1 .4 1.9.7 2.8a2 2 0 0 1-.5 2.1L8 9.9a16 16 0 0 0 6 6l1.3-1.3a2 2 0 0 1 2.1-.4c.9.3 1.8.6 2.8.7a2 2 0 0 1 1.7 2z"/></svg>
        055-210 384 671
      </li>
      <li>
        <svg viewBox="0 0 24 24" fill="none" stroke="currentColor" stroke-width="2" stroke-linejoin="round"><rect x="2" y="5" width="20" height="14"/><path d="M2 5l10 8 10-8"/></svg>
        hello@kestreltrade.com
      </li>
      <li>
        <svg viewBox="0 0 24 24" fill="none" stroke="currentColor" stroke-width="2"><circle cx="12" cy="12" r="10"/><path d="M2 12h20M12 2a15 15 0 0 1 0 20M12 2a15 15 0 0 0 0 20"/></svg>
        www.kestreltrade.com
      </li>
    </ul>
    <p class="address">318, Harbor Row Suite 4, Eastfield, 60214</p>
    <div class="edge-band"></div>
  </section>

</main>
</body>
</html>
```